House-share and Room Rental Website (With Focus on the Bedroom Landing Page)

Looking for website design for our House-share (executive accommodation) and room rental business.

Our company name is: Lodvenra could also be written as LodVenra or lodvenra. Either is fine .. just looking for a nice clean catchy logo to go with the design.

EXAMPLES
These are examples of other websites in this field that are doing well. this is a kind of baseline.
https://kelbrin.com.au/
https://www.tuvaplex.com/
https://www.nestorvi.com/
https://www.quillsa.net/
https://www.pendlebarrow.com.au/

Our business model is to rent rooms to people looking for high-quality accommodation. We fill the gap between those looking to rent rooms and those with rooms to rent. However, our model is slightly different from those already on the market as we looking to fill a massive gap in the market delivering upmarket rooms for rent.(Executive Accommodation) also in the back end will be coupled with a self management process in the back end.

We offer executive style accommodation that stands out above the rest. With special extras like fire safety.. and management processes that create happier homes. We are looking for a web design package that can help us grow and scale our business. We need a design that is captivating

Our MAIN focus is having a room landing page that stands out from the rest... The core of our business will rely on the promotion of the rooms in a share house... so the whole design relies on the BEDROOM landing page to drive results.

Target Market(s)

We have 2 markets we are aiming at ... the first market is people offering rooms to rent who want the highest rental return. The second market is people looking to rent safe, high-quality rooms, in houses that are well managed and looked after.

Industry/Entity Type

Share Economy

Logo Text

LodVenra

Number of Pages Required

5+ page

Font styles to use
Sans Serif

Colors
3276b5

Requirements
Must have
• A messaging system whereby we can create direct communication between those offering rooms and those looking for rooms.
• A call to action that says " Schedule an Inspection"
• Landing page for promoting rooms
• A home page for showing stock.
• Profile page for those selling rooms
• Profile page for those looking for rooms.
• A scheduling calendar for booking inspections
Nice to have
• Pages where new residents can lock in a room.. pay bond and rents.. and sign contracts
• Notifications
• SMS capabilities in the backend.
Should not have
• No script or handwriting fonts.

```html
<!DOCTYPE html>
<html lang="en">
<head>
<meta charset="utf-8">
<title>Lodvenra – Room Details</title>
<link rel="stylesheet" href="https://fonts.googleapis.com/css2?family=Lato:wght@400;700;900&family=Raleway:wght@500;600;700&display=swap">
<style>
:root{
  --blue:#1071c4;
  --red:#c8102e;
  --ink:#222;
  --text:#444;
  --line:#e4e4e4;
  --footer:#1f1f1f;
  --footer-field:#3a3a3a;
  --star:#f5b400;
  --btn-dark:#4a4a4a;
}
*{box-sizing:border-box;margin:0;padding:0}
html,body{width:1200px;height:3163px;overflow:hidden}
body{position:relative;background:#fff;font-family:"Lato",sans-serif;color:var(--text);font-size:12px}
.abs{position:absolute}
h1,h2,h3,h4{font-family:"Raleway",sans-serif;color:var(--ink)}
a{color:inherit;text-decoration:none}

/* header */
.site-header{left:0;top:0;width:1200px;height:99px;background:#fff}
.menu-grid{left:80px;top:38px;display:grid;grid-template-columns:repeat(3,5px);gap:4px}
.menu-grid i{width:5px;height:5px;background:#333;display:block}
.lang{left:122px;top:37px;font-size:11px;color:#555;display:flex;align-items:center;gap:6px}
.lang b{width:14px;height:9px;background:linear-gradient(#3a5fae 50%,#d33 50%);display:block}
.brand{display:flex;align-items:center;gap:8px}
.brand .mark{width:34px;height:34px;border-radius:50%;background:var(--blue)}
.brand .name{font-weight:700;font-size:28px;color:var(--blue);line-height:1}
.brand .tag{font-size:9px;color:#333;font-weight:700;letter-spacing:.3px;margin-top:2px}
.site-header .brand{left:510px;top:26px}
.btn{display:inline-flex;align-items:center;justify-content:center;border-radius:5px;font-size:11px;text-align:center}
.btn-primary{background:var(--blue);color:#fff}
.post-room{left:920px;top:31px;width:126px;height:30px}
.login{left:1057px;top:31px;width:63px;height:30px;border:1px solid #bbb;color:#333}

/* hero */
.hero{left:0;top:99px;width:1200px;height:420px;background:linear-gradient(100deg,#3b2d23 0%,#7d6a56 25%,#bfae96 45%,#8a7560 60%,#4e3f33 80%,#2a211b 100%)}
.hero-arrow{top:290px;color:#fff;font-size:26px}

/* room detail */
.gallery-main{left:80px;top:612px;width:519px;height:363px;background:linear-gradient(135deg,#5e1a1c,#8e3430 40%,#d9cbbd 72%,#7a3a26)}
.thumb{top:991px;width:118px;height:102px;background:linear-gradient(135deg,#6a2226,#a87c5e 60%,#4b2a1e)}
.detail{left:639px;top:622px;width:400px}
.detail .kind{font-size:11px;color:#333}
.detail .price{font-family:"Raleway",sans-serif;font-weight:700;font-size:19px;color:var(--red);margin-top:6px}
.detail .address{font-family:"Raleway",sans-serif;font-weight:700;font-size:19px;color:var(--ink);line-height:24px;margin-top:4px;width:300px}
.detail .meta{font-size:11px;color:#444;margin-top:6px}
.stars{color:var(--star);font-size:11px;letter-spacing:1px}
.detail .facts{font-size:11px;color:#333;margin-top:14px}
.detail hr{border:0;border-top:1px solid var(--line);margin:18px 0 14px;width:481px}
.detail h2{font-size:23px;font-weight:600;margin-bottom:6px}
.detail p{font-size:11.5px;line-height:16px;color:#333;width:481px}
.host{left:1060px;top:643px;width:80px;text-align:center;font-size:11px;color:#333}
.host .avatar{width:50px;height:50px;border-radius:50%;margin:0 auto 6px;background:linear-gradient(#8a5a40,#e7c4a6)}
.book{left:639px;top:1048px;width:198px;height:43px;font-size:14px}

.divider{left:80px;width:1040px;height:1px;background:var(--line)}

/* amenities */
.amenities{left:80px;top:1218px;width:1040px}
.amenities h2{font-size:24px;font-weight:600}
.amenities p{font-size:11.5px;line-height:16px;color:#333;margin-top:8px}
.amenity-row{left:80px;top:1322px}
.amenity{display:flex;align-items:center;gap:8px;font-size:11px;color:#333;position:absolute;top:0;white-space:nowrap}
.amenity svg{width:40px;height:40px;fill:#222}
.show-all{left:80px;top:1388px;font-size:11px;font-weight:700;color:#222;text-decoration:underline}

/* availability */
.availability{left:80px;top:1530px}
.availability h2{font-size:24px;font-weight:600}
.availability .sub{font-size:11px;color:#444;margin-top:14px;line-height:19px}
.calendar{top:1506px;width:365px;height:304px;background:#fff;box-shadow:0 2px 14px rgba(0,0,0,.1);border-radius:4px;padding:22px 24px}
.cal-head{display:flex;justify-content:space-between;align-items:center;font-family:"Raleway",sans-serif;font-weight:600;font-size:18px;color:var(--ink)}
.cal-head span{font-size:20px;width:16px}
.cal-grid{display:grid;grid-template-columns:repeat(7,1fr);row-gap:14px;margin-top:20px;text-align:center;font-size:10px;color:#333}
.cal-grid .dow{font-weight:700}
.cal-grid .d{width:24px;height:24px;line-height:24px;margin:-6px auto 0}
.cal-grid .hl{background:#ececec;border-radius:50%}

/* related */
.related-title{left:80px;top:1900px;font-size:24px;font-weight:600}
.related-nav{left:1085px;top:1898px;font-size:22px;font-weight:700;color:#222}
.related-nav b{color:var(--blue)}
.card{top:1966px;width:325px;height:413px;background:#fff;box-shadow:0 2px 12px rgba(0,0,0,.1)}
.card .photo{height:215px;position:relative}
.card .check{position:absolute;left:8px;top:8px;width:18px;height:18px;border:1.5px solid #fff;border-radius:2px}
.card .tag{position:absolute;left:0;top:173px;background:var(--blue);color:#fff;font-weight:900;font-size:19px;padding:6px 12px 6px 8px;line-height:26px}
.card .tag::after{content:"";position:absolute;right:-12px;top:0;border-left:12px solid var(--blue);border-top:19px solid transparent;border-bottom:19px solid transparent}
.card h3{font-size:14.5px;font-weight:700;color:var(--blue);margin:14px 0 0 18px}
.card .loc{display:flex;align-items:center;gap:6px;font-size:12px;color:#333;margin:14px 0 0 16px}
.card .stats{display:flex;justify-content:space-between;padding:0 38px 0 34px;margin-top:16px}
.stat{text-align:center;font-size:11px;color:#333}
.stat .ic{display:flex;align-items:center;justify-content:center;gap:4px;height:20px}
.stat .ic svg{width:20px;height:18px;fill:none;stroke:#333;stroke-width:1.6}
.card .browse{display:flex;align-items:center;justify-content:center;margin:10px auto 0;width:102px;height:26px;background:var(--btn-dark);color:#fff;border-radius:4px;font-size:11px}
.view-more{left:532px;top:2433px;width:130px;height:29px;font-size:11px}

/* newsletter */
.newsletter{left:0;top:2564px;width:1200px;text-align:center}
.newsletter h2{font-weight:500;font-size:24px}
.newsletter p{font-size:11px;color:#333;margin-top:10px}
.subscribe{left:342px;top:2651px;width:567px;height:39px;display:flex;box-shadow:0 2px 10px rgba(0,0,0,.08)}
.subscribe .field{flex:1;font-size:11px;color:#999;font-style:italic;padding:13px 22px}
.subscribe .btn{width:133px;border-radius:0 4px 4px 0;font-size:12px}

/* footer */
.site-footer{left:0;top:2752px;width:1200px;height:352px;background:var(--footer);color:#ddd}
.foot-about{left:80px;top:2918px;width:210px;font-size:12.5px;line-height:18px;color:#eee}
.socials{left:80px;top:3006px;display:flex;gap:10px}
.socials i{width:22px;height:22px;border-radius:50%;border:1.5px solid #ddd;display:block}
.socials i:first-child{background:var(--blue);border-color:var(--blue)}
.foot-col h4{color:#fff;font-size:15px;font-weight:600}
.foot-col h4::after{content:"";display:block;width:70px;height:3px;background:#fff;margin-top:14px}
.links{list-style:none;margin-top:20px}
.links li{font-size:11px;line-height:24px;color:#eee}
.links li::before{content:"›";margin-right:14px}
.contact-item{display:flex;gap:12px;font-size:13px;line-height:27px;color:#eee;margin-top:6px}
.contact-item svg{width:18px;height:18px;fill:#eee;margin-top:4px;flex:none}
.qc-field{position:absolute;background:var(--footer-field);color:#ccc;font-size:12px;padding:6px 12px}
.send{left:991px;top:3003px;width:129px;height:29px;font-size:12px}
.bottom-bar{left:0;top:3104px;width:1200px;height:59px;background:var(--blue);color:#fff;font-size:12px}
.bottom-bar .copy{position:absolute;left:80px;top:22px}
.cards{position:absolute;left:911px;top:20px;display:flex;gap:10px}
.cards i{width:33px;height:20px;background:#fff;border-radius:3px;display:block}
</style>
</head>
<body>

<header class="site-header abs">
  <div class="menu-grid abs"><i></i><i></i><i></i><i></i><i></i><i></i><i></i><i></i><i></i></div>
  <div class="lang abs"><b></b>Eng ▾</div>
  <div class="brand abs">
    <span class="mark"></span>
    <div><div class="name">Lodvenra</div><div class="tag">Executive Accommodation</div></div>
  </div>
  <a class="btn btn-primary post-room abs">Post Your Room</a>
  <a class="btn login abs">Log in</a>
</header>

<section class="hero abs" role="img" aria-label="Wide photo of an executive bedroom with twin beds, bedside lamps and an armchair"></section>
<span class="hero-arrow abs" style="left:30px">‹</span>
<span class="hero-arrow abs" style="left:1146px">›</span>

<div class="gallery-main abs" role="img" aria-label="Photo of a red-walled bedroom with two made beds"></div>
<div class="thumb abs" style="left:80px" role="img" aria-label="Thumbnail of lounge area"></div>
<div class="thumb abs" style="left:214px" role="img" aria-label="Thumbnail of armchair corner"></div>
<div class="thumb abs" style="left:348px" role="img" aria-label="Thumbnail of bedroom view"></div>
<div class="thumb abs" style="left:481px" role="img" aria-label="Thumbnail of bedside detail"></div>

<div class="detail abs">
  <div class="kind">Private Room in Apartment</div>
  <div class="price">Rental Price: $250</div>
  <div class="address">58 Carrow St, Elmsbury, VIC 3291</div>
  <div class="meta">Size of Room - 9' x 9' (2.74 x 2.75m)</div>
  <div class="meta"><span class="stars">★★★★★</span> (200 Views)</div>
  <div class="facts">2 Guests &nbsp; 1 Bedroom &nbsp; 1 Bed &nbsp; 1.5 Shared Baths</div>
  <hr>
  <h2>Room</h2>
  <p>Lorem Ipsum is simply dummy text of the printing and typesetting industry.industry Ipsum has been the industry's standard dummy text ever since the 1500s, when an unknown printer took a galley of type and scrambled it to make a type specimen book. It has survived not only five centuries,</p>
  <h2 style="margin-top:18px">The Space</h2>
  <p>Lorem Ipsum is simply dummy text of the printing and typesetting industry psum has industry Ipsum has been the industry's standard dummy text ever since the typeset 1500s,</p>
</div>
<div class="host abs"><div class="avatar" role="img" aria-label="Host profile photo"></div>Verity</div>
<a class="btn btn-primary book abs">Request to Book</a>

<div class="divider abs" style="top:1173px"></div>

<section class="amenities abs">
  <h2>ROOM Amenities</h2>
  <p>Lorem Ipsum is simply dummy text of the printing and typesetting industry. Lorem Ipsum has been the industry's standard dummy text ever since the 1500s, when an unknown printer took a galley of type and scrambled it to make a type specimen book. It has survived not only five centuries</p>
</section>
<div class="amenity-row abs">
  <div class="amenity" style="left:0"><svg viewBox="0 0 40 40"><path d="M14 6l6 6 6-6 1.5 1.5L22 13h14v20H4V13h14L12.5 7.5z M7 16v14h26V16z"/></svg>TV</div>
  <div class="amenity" style="left:127px"><svg viewBox="0 0 40 40"><path d="M6 4h28v32H6z M9 7v12h22V7z M9 22v11h22V22z M18 12h4v2h-4z M18 26h4v2h-4z" fill-rule="evenodd"/></svg>Storage Space</div>
  <div class="amenity" style="left:302px"><svg viewBox="0 0 40 40"><circle cx="14" cy="8" r="4"/><path d="M10 14h8l4 10h-4v10h-4V24h-4z M20 20h18v3h-2v13h-3V23H22z"/></svg>Study Desk</div>
  <div class="amenity" style="left:470px"><svg viewBox="0 0 40 40"><path d="M4 8h26v18H4z M7 11v12h20V11z M14 28h6v3h4v2H10v-2h4z M32 10h5v23h-5z" fill-rule="evenodd"/></svg>Workstation</div>
  <div class="amenity" style="left:635px"><svg viewBox="0 0 40 40"><path d="M8 8a4 4 0 018 0v12h20v3a8 8 0 01-8 8H12a8 8 0 01-8-8v-3h8V8a1 1 0 00-1 0v2H8z M10 34h3l-1 3h-3z M27 34h3l1 3h-3z"/></svg>Ensuite shower</div>
  <div class="amenity" style="left:789px"><svg viewBox="0 0 40 40"><circle cx="20" cy="20" r="12"/><circle cx="20" cy="20" r="8" fill="#fff"/><path d="M3 6h2v8h1V6h2v8a3 3 0 01-2 3v17H4V17a3 3 0 01-2-3V6zM35 6c2 0 3 4 3 10h-2v18h-2V6z"/></svg>Kitchenette</div>
</div>
<a class="show-all abs">Show all 12 Amenities</a>

<div class="divider abs" style="top:1449px"></div>

<section class="availability abs">
  <h2>Availability</h2>
  <div class="sub">Updated today<br>Available :Feb 23,2019 / Dec 10,2019</div>
</section>

<div class="calendar abs" style="left:356px">
  <div class="cal-head"><span>‹</span>February 2019<span></span></div>
  <div class="cal-grid">
    <div class="dow">SU</div><div class="dow">MO</div><div class="dow">TU</div><div class="dow">WE</div><div class="dow">TH</div><div class="dow">FR</div><div class="dow">SA</div>
    <div></div><div></div><div></div><div></div><div></div><div class="d">1</div><div class="d">2</div>
    <div class="d">3</div><div class="d">4</div><div class="d">5</div><div class="d">6</div><div class="d">7</div><div class="d">8</div><div class="d">9</div>
    <div class="d">10</div><div class="d">11</div><div class="d">12</div><div class="d">13</div><div class="d">14</div><div class="d">15</div><div class="d">16</div>
    <div class="d">17</div><div class="d">18</div><div class="d">19</div><div class="d">20</div><div class="d">21</div><div class="d">22</div><div class="d hl">23</div>
    <div class="d hl">24</div><div class="d hl">25</div><div class="d hl">26</div><div class="d hl">27</div><div class="d hl">28</div>
  </div>
</div>

<div class="calendar abs" style="left:753px">
  <div class="cal-head"><span></span>November 2019<span>›</span></div>
  <div class="cal-grid">
    <div class="dow">SU</div><div class="dow">MO</div><div class="dow">TU</div><div class="dow">WE</div><div class="dow">TH</div><div class="dow">FR</div><div class="dow">SA</div>
    <div></div><div></div><div></div><div></div><div></div><div class="d hl">1</div><div class="d hl">2</div>
    <div class="d hl">3</div><div class="d hl">4</div><div class="d hl">5</div><div class="d hl">6</div><div class="d hl">7</div><div class="d hl">8</div><div class="d hl">9</div>
    <div class="d">10</div><div class="d">11</div><div class="d">12</div><div class="d">13</div><div class="d">14</div><div class="d">15</div><div class="d">16</div>
    <div class="d">17</div><div class="d">18</div><div class="d">19</div><div class="d">20</div><div class="d">21</div><div class="d">22</div><div class="d">23</div>
    <div class="d">24</div><div class="d">25</div><div class="d">26</div><div class="d">27</div><div class="d">28</div><div class="d">29</div><div class="d">30</div>
  </div>
</div>

<div class="divider abs" style="top:1866px"></div>

<h2 class="related-title abs">Related Room</h2>
<div class="related-nav abs">‹ &nbsp;<b>›</b></div>

<article class="card abs" style="left:80px">
  <div class="photo" role="img" aria-label="Photo of a modern bedroom with blue feature wall" style="background:linear-gradient(135deg,#33506e,#8a8a86 45%,#d8d0c4 65%,#6b5a4a)">
    <span class="tag">$250</span>
  </div>
  <h3>Luxurious &amp; Stunning Room</h3>
  <div class="loc"><svg width="14" height="16" viewBox="0 0 14 16"><path d="M7 1a5 5 0 015 5c0 4-5 9-5 9S2 10 2 6a5 5 0 015-5z" fill="none" stroke="#555" stroke-width="1.4"/><circle cx="7" cy="6" r="1.8" fill="#555"/></svg>17 Wrenfield Road, Daltonvale, Australia</div>
  <div class="stats">
    <div class="stat"><div class="ic"><svg viewBox="0 0 20 18"><path d="M2 6l8-4 8 4v10H2z M6 16V9h8v7"/></svg>2</div>Rooms</div>
    <div class="stat"><div class="ic"><svg viewBox="0 0 20 18"><path d="M2 4v12 M2 11h16v5 M5 8h5v3 M11 8h7v3"/></svg>4</div>Bedrooms</div>
    <div class="stat"><div class="ic"><svg viewBox="0 0 20 18"><path d="M3 3h4v7 M2 10h16v3a3 3 0 01-3 3H5a3 3 0 01-3-3z"/></svg>2</div>Bath</div>
  </div>
  <a class="browse">Browse</a>
</article>

<article class="card abs" style="left:434px">
  <div class="photo" role="img" aria-label="Photo of a bright bedroom with canopy bed and ceiling fan" style="background:linear-gradient(135deg,#e9eef2,#cfd9e2 40%,#a8957c 72%,#e7e3dc)">
    <span class="check"></span>
    <span class="tag">$250</span>
  </div>
  <h3>Luxurious &amp; Stunning Room</h3>
  <div class="loc"><svg width="14" height="16" viewBox="0 0 14 16"><path d="M7 1a5 5 0 015 5c0 4-5 9-5 9S2 10 2 6a5 5 0 015-5z" fill="none" stroke="#555" stroke-width="1.4"/><circle cx="7" cy="6" r="1.8" fill="#555"/></svg>17 Wrenfield Road, Daltonvale, Australia</div>
  <div class="stats">
    <div class="stat"><div class="ic"><svg viewBox="0 0 20 18"><path d="M2 6l8-4 8 4v10H2z M6 16V9h8v7"/></svg>2</div>Rooms</div>
    <div class="stat"><div class="ic"><svg viewBox="0 0 20 18"><path d="M2 4v12 M2 11h16v5 M5 8h5v3 M11 8h7v3"/></svg>4</div>Bedrooms</div>
    <div class="stat"><div class="ic"><svg viewBox="0 0 20 18"><path d="M3 3h4v7 M2 10h16v3a3 3 0 01-3 3H5a3 3 0 01-3-3z"/></svg>2</div>Bath</div>
  </div>
  <a class="browse">Browse</a>
</article>

<article class="card abs" style="left:793px">
  <div class="photo" role="img" aria-label="Photo of a dark-walled bedroom with red cushions" style="background:linear-gradient(135deg,#3a2e26,#7a5e46 45%,#e2d6c6 70%,#5a4232)">
    <span class="check"></span>
    <span class="tag">$250</span>
  </div>
  <h3>Luxurious &amp; Stunning Room</h3>
  <div class="loc"><svg width="14" height="16" viewBox="0 0 14 16"><path d="M7 1a5 5 0 015 5c0 4-5 9-5 9S2 10 2 6a5 5 0 015-5z" fill="none" stroke="#555" stroke-width="1.4"/><circle cx="7" cy="6" r="1.8" fill="#555"/></svg>17 Wrenfield Road, Daltonvale, Australia</div>
  <div class="stats">
    <div class="stat"><div class="ic"><svg viewBox="0 0 20 18"><path d="M2 6l8-4 8 4v10H2z M6 16V9h8v7"/></svg>2</div>Rooms</div>
    <div class="stat"><div class="ic"><svg viewBox="0 0 20 18"><path d="M2 4v12 M2 11h16v5 M5 8h5v3 M11 8h7v3"/></svg>4</div>Bedrooms</div>
    <div class="stat"><div class="ic"><svg viewBox="0 0 20 18"><path d="M3 3h4v7 M2 10h16v3a3 3 0 01-3 3H5a3 3 0 01-3-3z"/></svg>2</div>Bath</div>
  </div>
  <a class="browse">Browse</a>
</article>

<a class="btn btn-primary view-more abs">View More</a>

<div class="divider abs" style="top:2514px"></div>

<section class="newsletter abs">
  <h2>Subscribe To Our Newsletter</h2>
  <p>To Receive The latest News And Update</p>
</section>
<div class="subscribe abs">
  <div class="field">Your E-Mail</div>
  <a class="btn btn-primary">Submit</a>
</div>

<footer class="site-footer abs"></footer>
<div class="brand abs" style="left:80px;top:2836px">
  <span class="mark"></span>
  <div><div class="name">Lodvenra</div><div class="tag" style="color:#fff">Executive Accommodation</div></div>
</div>
<p class="foot-about abs">Lorem Ipsum is simply dummy text of the printing and types tysetting industry...</p>
<div class="socials abs"><i></i><i></i><i></i><i></i><i></i></div>

<div class="foot-col abs" style="left:371px;top:2826px">
  <h4>Useful links</h4>
  <ul class="links">
    <li>Login</li><li>Register</li><li>My Profile</li><li>My Subscription</li><li>Privacy policy</li><li>Terms &amp; Conditions</li>
  </ul>
</div>

<div class="foot-col abs" style="left:576px;top:2826px;width:240px">
  <h4>Contact us</h4>
  <div class="contact-item" style="margin-top:16px"><svg viewBox="0 0 18 18"><path d="M9 2l8 7h-2v7h-4v-5H7v5H3V9H1z"/></svg><span>9 Tallowmere Place, Quenby<br>Western Australia.<br>ZipCode: 40821</span></div>
  <div class="contact-item"><svg viewBox="0 0 18 18"><path d="M2 7c0-3 3-4 7-4s7 1 7 4l-3 1-1-2H6L5 8z M4 10h10l2 5H2z"/></svg><span>555 014 2738</span></div>
  <div class="contact-item"><svg viewBox="0 0 18 18"><path d="M1 4h16v11H1z M3 6v7h12V6l-6 4z" fill-rule="evenodd"/></svg><span>info@lodvenra.com</span></div>
</div>

<div class="foot-col abs" style="left:890px;top:2826px">
  <h4>Quick Contact</h4>
</div>
<div class="qc-field" style="left:890px;top:2898px;width:111px;height:26px">Name</div>
<div class="qc-field" style="left:1008px;top:2898px;width:112px;height:26px">Phone</div>
<div class="qc-field" style="left:890px;top:2932px;width:230px;height:63px">Message</div>
<a class="btn btn-primary send abs">Send</a>

<div class="bottom-bar abs">
  <span class="copy">CopyRight © 2019 Lodvenra. All Right Reserve</span>
  <div class="cards"><i></i><i></i><i></i><i></i><i></i></div>
</div>

</body>
</html>
```